Play Equipment Distributor Website

We need a design (no coding) of a website for our play equipment sales company. The website will be in Japanese and is targeted at the Japanese market, and as such should be designed with that in mind.
The website will have 5 sections: home/top, products, safety, company information, contact. Initially we would like to have the top and Pebble Climb Works (our main product) pages designed. The main call to action - Request Catalog - should be present on all pages. The copy is still in the making, so please use Japanese dummy text to fill the pages for now.
For inspiration regarding the design, this is a website that we like very much: http://www.yardloopgear.example/
Attaching our logo, other graphics, as well as a rough idea of what we have on our mind in terms of layout and content of each page.
Target Market(s)
Japanese playset users - kindergartens, schools, entertainment parks, etc.

```html
<!DOCTYPE html>
<html lang="en">
<head>
<meta charset="utf-8">
<title>Kanata Play Japan</title>
<link href="https://fonts.googleapis.com/css2?family=Dosis:wght@400;500;600;700&display=swap" rel="stylesheet">
<style>
:root{
  --lime:#9ccb4b;
  --lime-dark:#8cbf3c;
  --leaf:#5e9a2c;
  --forest:#1f5e2e;
  --ink:#222;
  --muted:#666;
  --paper:#f7f7f7;
  --footer:#242424;
  --footer-bar:#eeeeee;
  --label:#3d3d3d;
}
*{box-sizing:border-box;margin:0;padding:0}
html,body{width:1200px;height:3261px;overflow:hidden}
body{font-family:'Dosis',sans-serif;color:var(--ink);background:#fff;position:relative}
.abs{position:absolute}
.topbar{left:0;top:0;width:1200px;height:30px;background:var(--lime);color:#fff;font-size:13px;text-align:right;padding:6px 90px 0 0}
.header{left:0;top:30px;width:1200px;height:118px;background:#fff}
.brand{left:80px;top:36px;display:flex;align-items:center;gap:14px;color:var(--leaf);font-size:30px;font-weight:600;line-height:1}
.brand .dot{width:34px;height:34px;border-radius:50%;background:var(--leaf)}
.nav{right:88px;top:52px;display:flex;gap:22px;font-size:13px;font-weight:600;color:#333;letter-spacing:.3px}
.hero{left:0;top:148px;width:1200px;height:487px;background:linear-gradient(180deg,#5fa8e6 0%,#a9d2f0 35%,#3f7a35 60%,#5c9a3c 100%)}
.hero-title{right:100px;top:290px;color:#fff;font-weight:700;font-size:54px;line-height:70px;text-align:right;text-shadow:0 2px 6px rgba(0,0,0,.35)}
.btn{display:flex;align-items:center;justify-content:center;background:#fff;color:#222;font-weight:500;box-shadow:0 2px 6px rgba(0,0,0,.25)}
.hero .btn{position:absolute;left:630px;top:330px;width:272px;height:63px;font-size:30px}
.photo-play{left:0;top:713px;width:617px;height:357px;background:linear-gradient(160deg,#7aa35a,#8a5a33 55%,#e9c220 85%,#6c8f48)}
.h2{font-size:40px;font-weight:700;text-align:center;color:#111}
.importance-title{left:660px;top:740px;width:400px}
.importance-copy{left:670px;top:840px;width:380px;font-size:13.5px;line-height:26px;color:var(--muted);text-align:center}
.deficit{left:0;top:1130px;width:1200px;height:555px;background:var(--paper)}
.deficit-title{left:0;top:1190px;width:1200px}
.deficit-copy{left:160px;top:1272px;width:880px;font-size:14px;line-height:27px;color:var(--muted);text-align:center}
.card{top:1365px;width:254px;height:237px;border-radius:12px;overflow:hidden;background:var(--lime)}
.card .pic{height:157px}
.card .name{height:80px;display:flex;align-items:center;justify-content:center;color:#fff;font-size:20px;font-weight:600}
.band{left:0;top:1685px;width:1200px;height:305px;background:linear-gradient(90deg,#1c5a2a,#246a34 50%,#1c5a2a)}
.band-copy{left:300px;top:1742px;width:600px;text-align:center;color:#fff;font-size:24px;line-height:40px}
.band .btn{position:absolute;left:470px;top:185px;width:270px;height:56px;font-size:24px}
.scallop{left:0;width:1200px;height:10px;background:radial-gradient(circle at 6px 0,transparent 5px,currentColor 5.5px) 0 0/12px 10px repeat-x}
.products-title{left:0;top:2018px;width:1200px}
.tile{overflow:hidden}
.tile .label{position:absolute;left:0;bottom:0;width:100%;padding:0 0 10px 22px;color:#fff;font-size:21px}
.tile.small{border:1px solid #ddd;background:#fff}
.tile.small .label{height:44px;padding:10px 0 0 16px;font-size:18px;background:var(--label)}
.cta-band{left:0;top:2811px;width:1200px;height:150px;background:linear-gradient(180deg,var(--lime),#b8dc7a)}
.cta-band .btn{position:absolute;left:460px;top:48px;width:270px;height:56px;font-size:24px}
.footer{left:0;top:2961px;width:1200px;height:252px;background:var(--footer);color:#ddd;font-size:12px}
.frow{position:absolute;left:0;width:1200px;display:flex;justify-content:center;align-items:center;gap:10px}
.social{position:absolute;left:470px;top:180px;display:flex;gap:14px}
.social span{width:40px;height:40px;border-radius:50%;background:#ddd}
.bottom{left:0;top:3213px;width:1200px;height:48px;background:var(--footer-bar);font-size:11.5px;color:#444}
.bottom .copy{position:absolute;left:92px;top:17px}
.bottom .links{position:absolute;right:100px;top:17px;display:flex;gap:28px}
</style>
</head>
<body>
<div class="abs topbar">Select Language EN &nbsp;|&nbsp; JP</div>
<header class="abs header"></header>
<div class="abs brand"><span class="dot"></span>Kanata Play Japan</div>
<nav class="abs nav"><span>HOME</span><span>PRODUCTS</span><span>SAFETY</span><span>ABOUT US</span><span>CONTACT US</span></nav>

<section class="abs hero" role="img" aria-label="Wooden playset with slide, swings and climbing wall on a lawn under blue sky">
  <a class="btn">Order Catalog</a>
</section>
<div class="abs hero-title">ACTIVE<br>ENRICHING PLAY !</div>

<div class="abs photo-play" role="img" aria-label="Children playing on a large wooden play structure with yellow slides"></div>
<h2 class="abs h2 importance-title">Importance of play</h2>
<p class="abs importance-copy">If your child can imagine it, wooden swingsets and playsets from Timberloop can make it real. Swings and monkey bars become amazing circus shows, rock climbing walls and rope ladders transform into Mount Everest. Timberloop outdoor wooden swing sets and playsets offer limitless possibilities for imagining, storytelling, games, exercise, and just plain fun. With so many opportunities for creative and active play, Timberloop gives your child the best swingset on the block.</p>

<section class="abs deficit"></section>
<h2 class="abs h2 deficit-title">Play deficit</h2>
<p class="abs deficit-copy">If your child can imagine it, wooden swingsets and playsets from Timberloop can make it real. Swings and monkey bars become amazing circus shows, rock climbing walls and rope ladders transform into Mount Everest.</p>
<div class="abs card" style="left:67px"><div class="pic" role="img" aria-label="Child on a yellow play panel" style="background:linear-gradient(135deg,#6d9b45,#e6c52b)"></div><div class="name">Physical Harm</div></div>
<div class="abs card" style="left:337px"><div class="pic" role="img" aria-label="Child looking through a red telescope toy" style="background:linear-gradient(135deg,#b9a489,#d9356a)"></div><div class="name">Intellectual Harm</div></div>
<div class="abs card" style="left:606px"><div class="pic" role="img" aria-label="Child standing in a wooden playhouse window" style="background:linear-gradient(135deg,#a56a35,#d9a25a)"></div><div class="name">Social Harm</div></div>
<div class="abs card" style="left:874px"><div class="pic" role="img" aria-label="Child playing tic-tac-toe panel" style="background:linear-gradient(135deg,#b8773b,#e6c35a)"></div><div class="name">Emotional Harm</div></div>

<section class="abs band" role="img" aria-label="Green tinted photo of children at play">
  <a class="btn">Request Catalog</a>
</section>
<div class="abs scallop" style="top:1685px;color:var(--forest);transform:scaleY(-1);top:1680px"></div>
<p class="abs band-copy">Solving the play deficit by providing fun and afordable play equipment!</p>

<h2 class="abs h2 products-title">Our Products</h2>
<div class="abs tile" style="left:159px;top:2135px;width:419px;height:315px;background:linear-gradient(160deg,#c9c3b8,#7a4e2c 50%,#f0c21c 80%,#3d5a32)" role="img" aria-label="Wooden playset with yellow tube slide"><span class="label">Pebble Climb Playsets</span></div>
<div class="abs tile" style="left:626px;top:2135px;width:420px;height:315px;background:linear-gradient(160deg,#d7dbe0,#8b5530 45%,#2b2b2b 85%)" role="img" aria-label="Crowd at a play event around a wooden play structure"><span class="label">Play Events</span></div>
<div class="abs tile small" style="left:159px;top:2478px;width:276px;height:266px"><div role="img" aria-label="Swing set with colourful roof" style="height:220px;background:linear-gradient(180deg,#fff,#e8d5c0 40%,#9a5a2c 75%,#fff)"></div><span class="label">Sky Hoppers</span></div>
<div class="abs tile small" style="left:463px;top:2478px;width:276px;height:266px"><div role="img" aria-label="Wooden play village with yellow slides" style="height:220px;background:linear-gradient(180deg,#fff,#c8905a 45%,#f0c21c 70%,#fff)"></div><span class="label">Playhamlet</span></div>
<div class="abs tile small" style="left:767px;top:2478px;width:277px;height:266px"><div role="img" aria-label="Large play structure with striped roofs" style="height:220px;background:linear-gradient(180deg,#fff,#e05a3a 35%,#f0c21c 60%,#fff)"></div><span class="label">Grand Town</span></div>

<section class="abs cta-band"><a class="btn">Request Catalog</a></section>
<div class="abs scallop" style="top:2811px;color:#fff"></div>

<footer class="abs footer">
  <div class="frow" style="top:35px">
    <svg width="14" height="18" viewBox="0 0 14 18"><path d="M7 0C3 0 0 3 0 7c0 5 7 11 7 11s7-6 7-11c0-4-3-7-7-7z" fill="#ddd"/><circle cx="7" cy="7" r="2.5" fill="#242424"/></svg>
    <span>Maple Bay, CA 90000, US 4321, Sample St</span></div>
  <div class="frow" style="top:79px">
    <svg width="18" height="18" viewBox="0 0 18 18"><circle cx="9" cy="9" r="8" fill="none" stroke="#ddd" stroke-width="1.6"/><path d="M9 4v5l3 2" stroke="#ddd" stroke-width="1.6" fill="none"/></svg>
    <span>Monday - Friday: 7:30 am - 17:00 pm, Saturday: 8:00 am - 15:00 pm</span></div>
  <div class="frow" style="top:122px">
    <svg width="12" height="18" viewBox="0 0 12 18"><rect x="1" y="1" width="10" height="16" rx="2" fill="none" stroke="#ddd" stroke-width="1.6"/><circle cx="6" cy="14" r="1" fill="#ddd"/></svg>
    <span>+1 000 555 0142, +1 000 555 0187</span></div>
  <div class="social"><span></span><span></span><span></span><span></span><span></span></div>
</footer>
<div class="abs bottom">
  <span class="copy">Copyrights © 2018 / All Rights Reserved</span>
  <div class="links"><span>Home</span><span>Products</span><span>Safety</span><span>About Us</span><span>Contact Us</span></div>
</div>
</body>
</html>
```